Meadowlark Suds Business Card

The new business card design will incorporate my new logo components designed by one of your designers. Meadowlark Suds creates high quality soaps and bath products. They would be suited for a Spa, Bed and Breakfast, Boutique environment. The look should be a white background.
Classy, soft and using the colour palet of the logo. The card will be two sided.
Updates

Target Market(s)

Looking to appeal to an upper end market. Spas, boutiques, independent gift stores, bridal salons, bed and breakfast, etc. I want the card to impart a sense of elegance, tranquility and Meadowlark. But also quality and value.

Industry/Entity Type

Business

Font styles to use
Sans Serif
Script

Requirements
Must have
• My logo on the front. But also on the back but faded out to allow written notes on the back.
On the front : Carla Penwick
Owner/Creator
47 Ashgrove Rd
Fernbury, Ont K4R 2P9
613.402.9186
Creating Quality Handcrafted Soaps And Bath Products
Custom and Wholesale Orders Welcome
Www.meadowlarksuds-example.ca
Www.facebook.com / MeadowlarkSudsandTub
info@meadowlarksuds-example.ca

```html
<!DOCTYPE html>
<html lang="en">
<head>
<meta charset="utf-8">
<title>Meadowlark Suds Business Card</title>
<link href="https://fonts.googleapis.com/css2?family=Great+Vibes&family=Lato:wght@400;700&display=swap" rel="stylesheet">
<style>
  :root {
    --page: #ecebe7;
    --card: #ffffff;
    --teal: #7aaea3;
    --teal-soft: #c9ded9;
    --blush: #efe1d6;
    --shadow: rgba(60, 50, 40, 0.18);
  }
  html, body {
    margin: 0;
    width: 1200px;
    height: 1023px;
    overflow: hidden;
    background: var(--page);
    font-family: "Lato", Arial, sans-serif;
    color: var(--teal);
  }
  .card-set {
    position: relative;
    width: 1200px;
    height: 1023px;
  }
  .card {
    position: absolute;
    top: 190px;
    width: 420px;
    height: 640px;
    background: var(--card);
    box-shadow: 0 12px 30px var(--shadow);
    box-sizing: border-box;
  }
  .card--back { left: 140px; }
  .card--front { left: 640px; }

  .faded-brand {
    position: absolute;
    left: 40px;
    top: 40px;
    width: 340px;
    height: 420px;
    border-radius: 48% 52% 40% 44%;
    background: radial-gradient(ellipse at 55% 40%, var(--teal-soft) 0%, var(--blush) 45%, rgba(255,255,255,0) 72%);
    opacity: 0.6;
  }
  .notes-title {
    position: absolute;
    top: 58px;
    left: 0;
    right: 0;
    text-align: center;
    font-family: "Great Vibes", cursive;
    font-size: 58px;
    margin: 0;
    font-weight: 400;
  }
  .tagline {
    position: absolute;
    left: 44px;
    bottom: 70px;
    margin: 0;
    font-size: 19px;
    line-height: 1.35;
    letter-spacing: 0.5px;
  }

  .brand {
    position: absolute;
    top: 120px;
    left: 0;
    right: 0;
    text-align: center;
  }
  .brand-dot {
    display: block;
    width: 60px;
    height: 60px;
    margin: 0 auto 20px;
    border-radius: 50%;
    background: var(--teal-soft);
  }
  .brand-name {
    font-size: 34px;
    font-weight: 400;
    letter-spacing: 1px;
    margin: 0;
  }
  .person {
    position: absolute;
    top: 340px;
    left: 0;
    right: 0;
    text-align: center;
  }
  .person-name {
    margin: 0;
    font-size: 34px;
    font-weight: 400;
    letter-spacing: 0.5px;
  }
  .person-role {
    margin: 2px 0 0;
    font-size: 17px;
    letter-spacing: 0.5px;
  }
  .address {
    position: absolute;
    top: 440px;
    left: 0;
    right: 0;
    text-align: center;
    font-style: normal;
    font-size: 18px;
    line-height: 1.35;
    letter-spacing: 0.5px;
  }
  .contacts {
    position: absolute;
    top: 520px;
    left: 82px;
    margin: 0;
    padding: 0;
    list-style: none;
    font-size: 16px;
    line-height: 1.55;
  }
  .contacts li {
    display: flex;
    align-items: center;
    gap: 7px;
  }
  .contacts svg { width: 15px; height: 15px; flex: none; }
  .icon-dot {
    width: 13px;
    height: 13px;
    border-radius: 50%;
    background: var(--teal);
    flex: none;
  }
</style>
</head>
<body>
<main class="card-set">
  <section class="card card--back" aria-label="Card back">
    <div class="faded-brand" role="img" aria-label="Faded Meadowlark Suds brand decoration"></div>
    <h2 class="notes-title">Notes:</h2>
    <p class="tagline">Creating Quality Handcrafted Soaps<br>And Bath Products</p>
  </section>

  <section class="card card--front" aria-label="Card front">
    <div class="brand">
      <span class="brand-dot"></span>
      <p class="brand-name">Meadowlark Suds</p>
    </div>
    <div class="person">
      <h1 class="person-name">Carla Penwick</h1>
      <p class="person-role">Owner/Creator</p>
    </div>
    <address class="address">47 Ashgrove Rd, Fernbury,<br>Ont K4R 2P9</address>
    <ul class="contacts">
      <li>
        <svg viewBox="0 0 24 24" aria-hidden="true"><path fill="#7aaea3" d="M6.6 10.8a15.1 15.1 0 0 0 6.6 6.6l2.2-2.2a1 1 0 0 1 1-.25 11.4 11.4 0 0 0 3.6.57 1 1 0 0 1 1 1V20a1 1 0 0 1-1 1A17 17 0 0 1 3 4a1 1 0 0 1 1-1h3.5a1 1 0 0 1 1 1c0 1.25.2 2.45.57 3.57a1 1 0 0 1-.25 1z"/></svg>
        613.402.9186
      </li>
      <li><span class="icon-dot"></span>www.meadowlarksuds-example.ca</li>
      <li><span class="icon-dot"></span>MeadowlarkSudsandTub</li>
    </ul>
  </section>
</main>
</body>
</html>
```